Harbor Business Cards

I need a business card designed with the following information.

Company Name: Harbor Wealth Management
Name: BriAnne Dockery
Title: Executive Assistant
Cell: (281) 555-0173
Direct Line: (832) 555-0148
Email: brianne@harborwmx.com
Address: 20537 W. Marlowe PKWY Ste. B
Tomball, TX 77390

I have attached the logo.
I would like it in navy blue and silver.
Thanks.

```html
<!DOCTYPE html>
<html lang="en">
<head>
<meta charset="utf-8">
<title>Harbor Wealth Management – Business Card</title>
<link rel="stylesheet" href="https://fonts.googleapis.com/css2?family=Cabin:wght@400;600&display=swap">
<style>
  :root {
    --navy: #0c1849;
    --card: #e5ecef;
    --silver: #c9cbcc;
    --backdrop: #3b3734;
  }
  * { margin: 0; padding: 0; box-sizing: border-box; }
  html, body {
    width: 1200px; height: 1200px; overflow: hidden;
    background: var(--backdrop);
    font-family: "Cabin", sans-serif;
    color: var(--navy);
  }
  .card {
    position: absolute;
    left: 173px;
    width: 854px;
    height: 500px;
    background: var(--card);
    border-radius: 50px 50px 50px 0;
    overflow: hidden;
  }
  .card--front { top: 73px; }
  .card--back { top: 626px; }

  .brand-mark {
    position: absolute;
    background: var(--navy);
    border-radius: 50%;
  }
  .card--front .brand-mark { left: 347px; top: 105px; width: 160px; height: 160px; }
  .card--back .brand-mark { left: 641px; top: 43px; width: 150px; height: 150px; background: var(--silver); }

  .wordmark { position: absolute; text-align: center; font-weight: 400; text-transform: uppercase; }
  .wordmark span { display: block; }
  .card--front .wordmark { left: 0; width: 854px; top: 330px; }
  .card--front .wordmark-name { font-size: 62px; letter-spacing: 0.5em; padding-left: 0.5em; line-height: 70px; }
  .card--front .wordmark-sub { font-size: 26px; letter-spacing: 0.42em; padding-left: 0.42em; margin-top: 16px; }
  .card--back .wordmark { left: 40px; width: 345px; top: 393px; }
  .card--back .wordmark-name { font-size: 40px; letter-spacing: 0.5em; padding-left: 0.5em; line-height: 46px; }
  .card--back .wordmark-sub { font-size: 16px; letter-spacing: 0.38em; padding-left: 0.38em; margin-top: 10px; }

  .accent-lines { position: absolute; left: 0; top: 0; }

  .contact { position: absolute; left: 376px; top: 150px; }
  .contact-name { font-size: 23px; font-weight: 600; }
  .contact-title { font-size: 18px; margin-top: 2px; }
  .contact-list { list-style: none; margin-top: 20px; font-size: 17.5px; line-height: 30px; }
</style>
</head>
<body>
  <section class="card card--front">
    <div class="brand-mark"></div>
    <div class="wordmark">
      <span class="wordmark-name">Harbor</span>
      <span class="wordmark-sub">Wealth Management</span>
    </div>
  </section>

  <section class="card card--back">
    <svg class="accent-lines" width="854" height="500" viewBox="0 0 854 500">
      <line x1="363" y1="0" x2="398" y2="136" stroke="#0c1849" stroke-width="4"/>
      <line x1="460" y1="370" x2="494" y2="502" stroke="#0c1849" stroke-width="4"/>
    </svg>
    <div class="brand-mark"></div>
    <div class="contact">
      <p class="contact-name">BriAnne Dockery</p>
      <p class="contact-title">Executive Assistant</p>
      <ul class="contact-list">
        <li>(281) 555-0173</li>
        <li>(832) 555-0148</li>
        <li>brianne@harborwmx.com</li>
        <li>20537 W. Marlowe PKWY Ste. B Tomball, TX 77390</li>
      </ul>
    </div>
    <div class="wordmark">
      <span class="wordmark-name">Harbor</span>
      <span class="wordmark-sub">Wealth Management</span>
    </div>
  </section>
</body>
</html>
```